Redesign a Shoplane store using the existing Arbor theme

Basically, the work that needs to be done is to fix the overall design, the store is a general store with different categories. Here is a link to all the categories we have https://files.quillpage.example/doc/7kTzmP2vWqLx9RbNc4YhJdE3sAf8GuV0oZi6KlMnQ-Rt/edit. We wanted all of these categories to fit in a mega menu however we also want it not to cover the entire slider below the navigation menu because at the moment since there are so many categories, it makes the mega menu to be too long which makes it cover the entire slider. We also want HD quality images for the slider, the slider images must be images based on the collections that we have. Another task is to improve the loading speed of the theme.
Also take note, to make the design look feminine as most of our audience will be mostly women. Lastly, add slides on the main page with pictures that are relevant to each category, for example the baby category has a family picture in there and etc...
Target Market(s)
Women all over the world
Industry/Entity Type
Ecommerce
Font styles to use
Other font styles liked:
- Montserat
Requirements
Must have
- high quality images, mega menus for each of the category and collections
Nice to have
- great logo and favicon
Should not have
- bad colors

```html
<!DOCTYPE html>
<html lang="en">
<head>
<meta charset="utf-8">
<title>Rosellyn — Home</title>
<link href="https://fonts.googleapis.com/css2?family=Montserrat:ital,wght@0,400;0,500;0,600;0,700;1,400&display=swap" rel="stylesheet">
<style>
  :root {
    --rose: #d98f94;
    --rose-deep: #c97a80;
    --rose-band: #dea0a3;
    --rose-soft: #f2d3d3;
    --ink: #111111;
    --text: #555555;
    --white: #ffffff;
    --line: #e8c3c5;
  }
  * { margin: 0; padding: 0; box-sizing: border-box; }
  html, body { width: 1200px; height: 2609px; overflow: hidden; }
  body { position: relative; background: var(--white); font-family: "Montserrat", sans-serif; color: var(--text); }
  .abs { position: absolute; }

  /* header */
  .announcement { left: 0; right: 0; top: 9px; text-align: center; font-size: 12px; color: var(--rose-soft); color: #e6a9ad; }
  .announcement svg { vertical-align: -2px; margin-right: 6px; }
  .social { left: 18px; top: 48px; display: flex; gap: 10px; }
  .social span { width: 12px; height: 12px; border-radius: 50%; background: var(--rose); display: block; }
  .brand { left: 0; right: 0; top: 34px; text-align: center; font-size: 36px; font-weight: 700; color: var(--rose); letter-spacing: 1px; }
  .search { left: 1139px; top: 47px; }
  .cart { left: 1162px; top: 35px; width: 38px; height: 40px; background: var(--rose); display: flex; align-items: center; justify-content: center; }
  .nav { left: 0; right: 0; top: 110px; display: flex; justify-content: center; gap: 14px; font-size: 13.5px; font-weight: 600; color: var(--rose); }
  .nav span svg { margin-left: 6px; vertical-align: 1px; }

  /* hero */
  .hero { left: 0; top: 142px; width: 1200px; height: 603px; background: linear-gradient(100deg, #f6dcdb 0%, #efc8c8 45%, #c98e90 70%, #a2676b 100%); }
  .hero-copy { left: 37px; top: 348px; }
  .hero-copy h1 { font-size: 34px; font-weight: 700; color: var(--ink); }
  .hero-copy p { font-size: 17px; color: var(--ink); margin-top: 12px; }
  .hero-copy .btn-outline { margin-top: 18px; width: 205px; height: 28px; border: 1px solid #333; border-radius: 14px; display: flex; align-items: center; justify-content: center; font-size: 13px; color: #333; }
  .arrow-btn { width: 36px; height: 36px; border-radius: 50%; background: rgba(255,255,255,.85); display: flex; align-items: center; justify-content: center; }
  .dots { left: 585px; top: 702px; display: flex; gap: 14px; }
  .dots span { width: 8px; height: 8px; border-radius: 50%; background: #b27a7d; }
  .dots span.on { background: #333; }

  /* gallery */
  .section-title { left: 0; right: 0; text-align: center; font-size: 31px; font-weight: 600; color: var(--rose); }
  .rule { left: 570px; width: 60px; height: 1px; background: var(--rose); }
  .gallery { left: 100px; top: 865px; width: 1000px; height: 300px; overflow: hidden; }
  .product { position: absolute; top: 0; width: 233px; text-align: center; }
  .product .shot { width: 233px; height: 233px; }
  .product .name { margin-top: 16px; font-size: 12.5px; color: var(--rose); line-height: 15px; }
  .product .price { font-size: 12.5px; color: #444; margin-top: 2px; }
  .product .price i { font-size: 11px; }
  .product .price s { color: var(--line); font-size: 11px; margin-left: 4px; }
  .sale { position: absolute; right: 6px; top: 6px; width: 42px; height: 42px; border-radius: 50%; background: var(--rose); color: #fff; font-size: 9px; display: flex; align-items: center; justify-content: center; }

  /* feature */
  .feature-img { left: 108px; top: 1223px; width: 484px; height: 375px; background: linear-gradient(135deg, #c99092, #9a6266 55%, #7d4d51); }
  .feature-copy { left: 625px; top: 1330px; width: 440px; }
  .feature-copy h2 { font-size: 31px; font-weight: 600; color: var(--rose); }
  .feature-copy p { margin-top: 18px; font-size: 12.5px; line-height: 19px; color: #444; }
  .pill { display: inline-flex; align-items: center; justify-content: center; height: 26px; padding: 0 13px; border-radius: 13px; background: var(--rose); color: #fff; font-size: 12.5px; margin-top: 20px; }

  /* subscribe */
  .subscribe { left: 0; top: 1632px; width: 1200px; height: 245px; background: var(--rose-band); }
  .subscribe h2 { position: absolute; left: 0; right: 0; top: 30px; text-align: center; font-size: 31px; font-weight: 700; color: #fff; }
  .subscribe .lead { position: absolute; left: 0; right: 0; top: 87px; text-align: center; font-size: 12.5px; color: #fff; }
  .field { position: absolute; height: 26px; border: 1px solid #fff; border-radius: 13px; background: #fff; font-size: 12.5px; color: #bbb; padding-left: 13px; display: flex; align-items: center; }
  .signup { position: absolute; left: 760px; top: 168px; width: 122px; height: 28px; border: 1.5px solid #fff; border-radius: 14px; color: #fff; font-size: 13px; display: flex; align-items: center; justify-content: center; }

  /* categories */
  .category { position: absolute; top: 1911px; width: 340px; text-align: center; }
  .category .shot { margin: 0 auto; height: 246px; }
  .category h3 { margin-top: 22px; font-size: 31px; font-weight: 600; color: var(--rose); line-height: 40px; }
  .category .btn-rose { margin: 16px auto 0; width: 118px; height: 29px; border: 1.5px solid var(--rose); border-radius: 15px; color: var(--rose); font-size: 12.5px; display: flex; align-items: center; justify-content: center; }

  /* footer */
  .footer { left: 0; top: 2306px; width: 1200px; height: 303px; background: var(--rose-band); }
  .footer-mark { position: absolute; left: 520px; top: 18px; width: 160px; height: 96px; display: flex; align-items: center; justify-content: center; font-size: 26px; font-weight: 400; color: #333; }
  .footer-note { position: absolute; left: 0; right: 0; top: 145px; text-align: center; font-size: 12.5px; line-height: 19px; color: #fff; }
  .footer-note b { font-weight: 700; }
  .copyright { position: absolute; left: 0; right: 0; top: 229px; text-align: center; font-size: 10.5px; color: #fff; }
  .payments { position: absolute; left: 393px; top: 261px; display: flex; gap: 5px; }
  .payments span { width: 30px; height: 19px; border-radius: 3px; background: #fff; }
  .payments span:nth-child(odd) { background: #f6eded; }
  .currency { position: absolute; left: 8px; top: 227px; width: 92px; height: 33px; background: #fff; border-radius: 3px; display: flex; align-items: center; gap: 8px; padding-left: 12px; font-size: 12px; color: #333; }
  .currency .flag { width: 24px; height: 15px; background: linear-gradient(#c0392b 0 50%, #2c4a8a 50%); }
  .captcha { position: absolute; left: 1142px; top: 2547px; width: 58px; height: 52px; background: #f9f9f9; box-shadow: 0 0 4px rgba(0,0,0,.25); }
</style>
</head>
<body>

  <div class="abs announcement">
    <svg width="13" height="11" viewBox="0 0 13 11"><path d="M6.5 11 1 5.5A3 3 0 0 1 6.5 1.6 3 3 0 0 1 12 5.5z" fill="#e6a9ad"/></svg>We are still shipping weekly! Hope everyone is staying safe.
  </div>

  <div class="abs social" aria-label="Social links"><span></span><span></span><span></span><span></span><span></span><span></span></div>
  <div class="abs brand">Rosellyn</div>
  <svg class="abs search" width="14" height="14" viewBox="0 0 14 14"><circle cx="6" cy="6" r="5" fill="none" stroke="#777" stroke-width="1.3"/><line x1="9.7" y1="9.7" x2="13.5" y2="13.5" stroke="#777" stroke-width="1.3"/></svg>
  <div class="abs cart"><svg width="16" height="14" viewBox="0 0 16 14"><path d="M0 1h3l2 8h8l2-6H4.5" fill="none" stroke="#fff" stroke-width="1.6"/><circle cx="6" cy="12" r="1.3" fill="#fff"/><circle cx="12" cy="12" r="1.3" fill="#fff"/></svg></div>

  <nav class="abs nav">
    <span>Bags<svg width="11" height="6" viewBox="0 0 11 6"><path d="M.5.5l5 5 5-5" fill="none" stroke="#d98f94"/></svg></span>
    <span>Beauty &amp; Wellness<svg width="11" height="6" viewBox="0 0 11 6"><path d="M.5.5l5 5 5-5" fill="none" stroke="#d98f94"/></svg></span>
    <span>Lifestyle<svg width="11" height="6" viewBox="0 0 11 6"><path d="M.5.5l5 5 5-5" fill="none" stroke="#d98f94"/></svg></span>
    <span>Cosmetic Organizers<svg width="11" height="6" viewBox="0 0 11 6"><path d="M.5.5l5 5 5-5" fill="none" stroke="#d98f94"/></svg></span>
    <span>FAQs</span>
    <span>Track Your Order</span>
  </nav>

  <section class="abs hero" role="img" aria-label="Rose-toned flat lay of lipsticks, eyeshadow palette, brushes and a quilted cosmetic bag on white wood with roses"></section>
  <div class="abs hero-copy">
    <h1>Cosmetic Organizers</h1>
    <p>Additional info in the subheading</p>
    <div class="btn-outline">Shop Now</div>
  </div>
  <div class="abs arrow-btn" style="left:8px;top:687px"><svg width="16" height="12" viewBox="0 0 16 12"><path d="M15 6H1M6 1 1 6l5 5" fill="none" stroke="#333" stroke-width="1.4"/></svg></div>
  <div class="abs arrow-btn" style="left:1155px;top:687px"><svg width="16" height="12" viewBox="0 0 16 12"><path d="M1 6h14M10 1l5 5-5 5" fill="none" stroke="#333" stroke-width="1.4"/></svg></div>
  <div class="abs dots"><span></span><span class="on"></span></div>

  <h2 class="abs section-title" style="top:776px">From the Gallery</h2>
  <div class="abs rule" style="top:830px"></div>

  <div class="abs gallery">
    <div class="product" style="left:-135px">
      <div class="shot" role="img" aria-label="White cosmetic storage box with drawers" style="background:linear-gradient(#fff,#ececee 60%,#dcdcdf)"></div>
      <div class="name">Lipstick &amp; Jewelry<br>Organizer</div>
      <div class="price">$39.99</div>
    </div>
    <div class="product" style="left:134px">
      <div class="shot" role="img" aria-label="Clear acrylic lipstick tower holding red and gold lipsticks" style="background:linear-gradient(135deg,#e9dccb,#c98d6e 50%,#8d5a3f)"></div>
      <div class="name">Acrylic Clear Lipstick Stand Holder</div>
      <div class="price"><i>from</i> $22.99</div>
    </div>
    <div class="product" style="left:383px">
      <div class="shot" role="img" aria-label="White makeup tray holding small toiletry bottles" style="background:linear-gradient(#eef1f4,#dfe5ea)"></div>
      <div class="sale">Sale</div>
      <div class="name">Travel Makeup LED Light Up Mirror</div>
      <div class="price">$60.99<s>$121.99</s></div>
    </div>
    <div class="product" style="left:633px">
      <div class="shot" role="img" aria-label="Promotional image of an LED makeup box filled with cosmetics" style="background:linear-gradient(#2b2b2b,#4a4a4a 60%,#1c1c1c)"></div>
      <div class="name">The Ultimate LED Makeup Box</div>
      <div class="price">$149.99</div>
    </div>
    <div class="product" style="left:887px">
      <div class="shot" role="img" aria-label="White stacking drawer organizer" style="background:linear-gradient(#fff 30%,#e6e6e8 50%,#fff 75%)"></div>
      <div class="name">Space Saving Cosmetic<br>Organizer</div>
      <div class="price"><i>from</i> $19.99</div>
    </div>
  </div>
  <div class="abs arrow-btn" style="left:108px;top:1000px;background:#fff;box-shadow:0 1px 3px rgba(0,0,0,.15)"><svg width="14" height="10" viewBox="0 0 14 10"><path d="M13 5H1M5 1 1 5l4 4" fill="none" stroke="#333" stroke-width="1.3"/></svg></div>
  <div class="abs arrow-btn" style="left:1055px;top:1000px;background:#fff;box-shadow:0 1px 3px rgba(0,0,0,.15)"><svg width="14" height="10" viewBox="0 0 14 10"><path d="M1 5h12M9 1l4 4-4 4" fill="none" stroke="#333" stroke-width="1.3"/></svg></div>

  <div class="abs feature-img" role="img" aria-label="Rose-toned flat lay of a straw hat, shirt, glasses, camera, belt and leather shoes"></div>
  <div class="abs feature-copy">
    <h2>Heading text here</h2>
    <p>Use this text to share information about your brand with your customers. Describe a product, share announcements, or welcome customers to your store.</p>
    <div class="pill">View all</div>
  </div>

  <section class="abs subscribe">
    <h2>Subscribe</h2>
    <div class="lead">Sign up to get the latest on sales, new releases and more …</div>
    <div class="field" style="left:308px;top:122px;width:282px">First Name</div>
    <div class="field" style="left:600px;top:122px;width:282px">Last Name</div>
    <div class="field" style="left:308px;top:168px;width:442px">Email*</div>
    <div class="signup">Sign Up</div>
  </section>

  <div class="category" style="left:96px">
    <div class="shot" role="img" aria-label="Metallic rose cosmetic pouch" style="width:270px;background:radial-gradient(ellipse at center,#e7b2b4 0%,#d69498 45%,#fff 72%)"></div>
    <h3>Bags</h3>
    <div class="btn-rose">View products</div>
  </div>
  <div class="category" style="left:430px">
    <div class="shot" role="img" aria-label="Makeup brushes standing in a holder" style="width:316px;background:linear-gradient(135deg,#f3d6d6,#d9a2a5 55%,#a86d72)"></div>
    <h3>Brush Holders</h3>
    <div class="btn-rose">View products</div>
  </div>
  <div class="category" style="left:763px">
    <div class="shot" role="img" aria-label="Bundle of wavy hair extensions" style="width:170px;background:radial-gradient(ellipse at center,#8d4a4e 0%,#6e3337 55%,#fff 72%)"></div>
    <h3>Hair</h3>
    <div class="btn-rose">View products</div>
  </div>

  <footer class="abs footer">
    <div class="footer-mark">Atelier</div>
    <div class="footer-note">All the lovely products in this demo shop are courtesy of &nbsp;artist <b>Clara Bennett</b>.<br>To purchase, please visit <i>Petal + Finch</i>.</div>
    <div class="copyright">© 2020 Rosellyn. Powered by Shoplane</div>
    <div class="payments" aria-label="Accepted payment methods"><span></span><span></span><span></span><span></span><span></span><span></span><span></span><span></span><span></span><span></span><span></span><span></span></div>
    <div class="currency"><span class="flag" role="img" aria-label="Currency flag"></span>USD <svg width="8" height="5" viewBox="0 0 8 5"><path d="M.5.5l3.5 3.5 3.5-3.5" fill="none" stroke="#333"/></svg></div>
  </footer>
  <div class="captcha" aria-hidden="true"></div>

</body>
</html>
```